Bramble Nook Complementary Pass

I’d like a complimentary pass for any 30-minute Bramble Nook session. Choose one of the following options: Infrared Sauna with Red Light, Massage Chair Velquist Compression Therapy, or Paraffin Wax Hand Bath.

Please incorporate the logo and brand colors into your design. I’d like a square image that will be printed on square business cards (no rectangles).

Please refer to the logo and menu for more details.

See discretion

```html
<!DOCTYPE html>
<html lang="en">
<head>
<meta charset="utf-8">
<title>Bramble Nook Complimentary Pass</title>
<link rel="stylesheet" href="https://fonts.googleapis.com/css2?family=Montserrat:wght@400;500;600&family=Playfair+Display:wght@400&family=Sacramento&display=swap">
<style>
  :root {
    --backdrop: #b4b4b4;
    --card-white: #ffffff;
    --ink-navy: #2a2273;
    --brand-purple: #4a3390;
    --brand-orange: #f0603f;
    --dark-top: #8a8a8a;
    --dark-bottom: #0e0e0e;
  }
  * { box-sizing: border-box; margin: 0; padding: 0; }
  html, body { width: 1200px; height: 960px; overflow: hidden; }
  body {
    background: var(--backdrop);
    font-family: "Montserrat", sans-serif;
    position: relative;
  }
  .card {
    position: absolute;
    top: 281px;
    width: 399px;
    height: 399px;
    border-radius: 18px;
    overflow: hidden;
  }
  .card-front { left: 166px; }
  .card-back { left: 635px; background: var(--card-white); color: var(--ink-navy); }

  /* front */
  .front-pattern {
    position: absolute; inset: 0;
    background: linear-gradient(135deg, var(--dark-top) 0%, #3a3a3a 45%, var(--dark-bottom) 80%);
  }
  .front-brand {
    position: absolute;
    left: 0; right: 0; top: 150px;
    text-align: center;
    color: var(--brand-purple);
    font-weight: 600;
    font-size: 40px;
    line-height: 1.15;
    letter-spacing: 1px;
  }
  .front-brand .dot {
    display: inline-block;
    width: 16px; height: 16px;
    border-radius: 50%;
    background: var(--brand-orange);
    margin-right: 10px;
    vertical-align: middle;
  }

  /* back */
  .back-brand {
    position: absolute; top: 30px; left: 0; right: 0;
    text-align: center;
    color: var(--brand-purple);
    font-weight: 600;
    font-size: 15px;
    line-height: 1.2;
  }
  .back-brand .dot {
    display: block;
    width: 14px; height: 14px;
    margin: 0 auto 6px;
    border-radius: 50%;
    background: var(--brand-orange);
  }
  .pass-title {
    position: absolute; top: 74px; left: 0; right: 0;
    text-align: center;
    font-family: "Playfair Display", serif;
    font-size: 38px;
    line-height: 1;
    color: var(--ink-navy);
  }
  .pass-script {
    position: absolute; top: 106px; left: 0; right: 0;
    text-align: center;
    font-family: "Sacramento", cursive;
    font-size: 26px;
    line-height: 1;
    color: var(--ink-navy);
  }
  .entitles {
    position: absolute; top: 140px; left: 0; right: 0;
    text-align: center; font-size: 11px;
  }
  .offer {
    position: absolute; top: 157px; left: 0; right: 0;
    text-align: center;
    font-weight: 600; font-size: 16px; line-height: 1.05;
    color: var(--ink-navy);
  }
  .offer .accent { color: var(--brand-orange); }
  .choose {
    position: absolute; top: 198px; left: 35px; right: 57px;
    display: flex; align-items: flex-end; gap: 2px;
    font-size: 10px; font-weight: 500;
    color: var(--brand-orange);
    white-space: nowrap;
  }
  .choose .blank { flex: 1; border-bottom: 1px solid var(--ink-navy); height: 1px; margin-bottom: 2px; }
  .options { position: absolute; left: 35px; top: 215px; list-style: none; }
  .options li {
    display: flex; align-items: center; gap: 8px;
    height: 25.3px; font-size: 10.5px;
  }
  .tick { width: 12px; height: 12px; flex: none; }
  .terms {
    position: absolute; left: 0; right: 0; bottom: 0; height: 89px;
    background: var(--brand-purple); color: var(--card-white);
  }
  .terms-title {
    position: absolute; top: 5px; left: 0; right: 0;
    text-align: center; font-size: 10.5px; font-weight: 500;
    color: var(--brand-orange);
  }
  .term { position: absolute; top: 24px; font-size: 10.5px; line-height: 1.25; }
  .term .tick { display: block; margin-bottom: 3px; }
  .term-one { left: 28px; text-align: center; }
  .term-one .tick { margin-left: auto; margin-right: auto; }
  .term-two { left: 144px; }
  .term-two .tick { margin-left: 27px; }
  .term-three { left: 302px; }
  .term-three .tick { margin-left: 28px; }
</style>
</head>
<body>
  <svg width="0" height="0" style="position:absolute">
    <symbol id="tick-icon" viewBox="0 0 12 12">
      <circle cx="6" cy="6.5" r="4.8" fill="none" stroke="currentColor" stroke-width="1.2"/>
      <path d="M3.6 6.4 L5.6 8.4 L10.8 1.4" fill="none" stroke="currentColor" stroke-width="1.3" stroke-linecap="round"/>
    </symbol>
  </svg>

  <section class="card card-front">
    <div class="front-pattern" role="img" aria-label="Repeating brand symbol pattern fading from silver to black"></div>
    <div class="front-brand"><span class="dot"></span>Solvia<br>Physical Therapy</div>
  </section>

  <section class="card card-back">
    <div class="back-brand"><span class="dot"></span>Solvia Physical Therapy</div>
    <h1 class="pass-title">complimentary</h1>
    <div class="pass-script">pass</div>
    <p class="entitles">This card entitles you to</p>
    <p class="offer">ANY ONE <span class="accent">30-MIUTE</span><br>BRAMBLE NOOK SESSION</p>
    <div class="choose"><span>CHOSSE ONE OF THE FOLLOWING:</span><span class="blank"></span></div>
    <ul class="options">
      <li><svg class="tick" style="color:var(--brand-orange)"><use href="#tick-icon"/></svg>Infrared Sauna + Red Light</li>
      <li><svg class="tick" style="color:var(--brand-orange)"><use href="#tick-icon"/></svg>Massage Chair</li>
      <li><svg class="tick" style="color:var(--brand-orange)"><use href="#tick-icon"/></svg>Velquist Compression Therapy</li>
      <li><svg class="tick" style="color:var(--brand-orange)"><use href="#tick-icon"/></svg>Paraffin Wax Hand Bath</li>
    </ul>
    <div class="terms">
      <div class="terms-title">TERMS &amp; CONDITIONS</div>
      <div class="term term-one"><svg class="tick" style="color:var(--brand-orange)"><use href="#tick-icon"/></svg>One-time<br>use only</div>
      <div class="term term-two"><svg class="tick" style="color:var(--brand-orange)"><use href="#tick-icon"/></svg>Not redeeable<br>for cash</div>
      <div class="term term-three"><svg class="tick" style="color:var(--brand-orange)"><use href="#tick-icon"/></svg>Must present<br>this card at<br>time of visit</div>
    </div>
  </section>
</body>
</html>
```